The Linden Rooms. Psychotherapy practice. Looking for a multi-use design.

Hello, we need someone who can give us a design that's usable across business cards, rack cards and headed paper.
We're also looking for a logo that can be used on the cards and on the web site when we change the web site.
The current web site, www.the-linden-rooms.example.co.uk can be used to gather info, but does not need to be used for colour/design choices (e.g. one partner likes the Times font another prefers a sans-serif font. One likes the idea of a brass plaque in the design, the other doesn't).
The main point about the design is that it should convey an image of a professional service - their latest strap line is "Professional • Experienced • Confidential" used in a local ad.
Updates
The ladies have also asked me to add that although the Practice is very close to Marsh Priory, and one of the lines they use on the site is "Just a short walk from the Priory", they don't want it to look like something that's Christian or religious.
Thanks.

```html
<!DOCTYPE html>
<html lang="en">
<head>
<meta charset="utf-8">
<title>The Linden Rooms – Card</title>
<link rel="stylesheet" href="https://fonts.googleapis.com/css2?family=Barlow+Condensed:wght@300;600&display=swap">
<style>
  :root {
    --sky: #5ac8e8;
    --sky-light: #7fd3ef;
    --white: #ffffff;
    --ink: #6b5c55;
  }
  html, body {
    margin: 0;
    padding: 0;
    overflow: hidden;
    background: var(--sky);
  }
  .card {
    position: relative;
    width: 1200px;
    height: 777px;
    background: var(--sky);
    overflow: hidden;
    font-family: "Barlow Condensed", "Arial Narrow", sans-serif;
    color: var(--white);
  }
  .corner-accent {
    position: absolute;
    top: 0;
    right: 0;
  }
  .brand-mark {
    position: absolute;
    left: 540px;
    top: 200px;
  }
  .brand-name {
    position: absolute;
    top: 328px;
    left: 0;
    width: 100%;
    margin: 0;
    text-align: center;
    font-weight: 600;
    font-size: 66px;
    line-height: 1;
  }
  .brand-service {
    position: absolute;
    top: 405px;
    left: 0;
    width: 100%;
    margin: 0;
    text-align: center;
    font-weight: 300;
    font-size: 38px;
    line-height: 1;
    letter-spacing: 0.01em;
  }
  .strapline {
    position: absolute;
    top: 562px;
    left: 0;
    width: 100%;
    margin: 0;
    text-align: center;
    font-weight: 300;
    font-size: 45px;
    line-height: 1;
  }
  .strapline .dot { font-size: 30px; vertical-align: 0.18em; padding: 0 10px; }
  .rule {
    position: absolute;
    top: 630px;
    left: 117px;
    width: 965px;
    height: 2px;
    background: var(--white);
    border: 0;
    margin: 0;
  }
  .contact {
    position: absolute;
    top: 663px;
    left: 0;
    width: 100%;
    margin: 0;
    text-align: center;
    font-weight: 300;
    font-size: 34px;
    line-height: 1;
    color: var(--ink);
  }
  .contact .dot { font-size: 24px; vertical-align: 0.18em; padding: 0 8px; }
</style>
</head>
<body>
  <main class="card">
    <svg class="corner-accent" width="460" height="420" viewBox="0 0 460 420" aria-hidden="true">
      <circle cx="300" cy="150" r="230" fill="var(--sky-light)" opacity="0.55"/>
    </svg>

    <svg class="brand-mark" width="120" height="120" viewBox="0 0 120 120" aria-hidden="true">
      <circle cx="60" cy="60" r="54" fill="none" stroke="var(--white)" stroke-width="8"/>
    </svg>

    <h1 class="brand-name">The Linden Rooms</h1>
    <p class="brand-service">PSYCHOTHERAPY &amp; COUNSELLING</p>

    <p class="strapline">Professional<span class="dot">•</span>Experienced<span class="dot">•</span>Confidential</p>

    <hr class="rule">

    <p class="contact">The Linden Rooms, 8 Wick Lane, Marsh, MS2 4LR<span class="dot">•</span>www.the-linden-rooms.example.co.uk</p>
  </main>
</body>
</html>
```